Design eBook Cover for Homeowner Association (HOA) book

We need a cover design for an eBook entitled "The Civic Panel Volunteer's Primer: Self-Direction Hints and Sound Routines".

Title: The Civic Panel Volunteer's Primer

Subtitle: Self-Direction Hints and Sound Routines

Name of Author: Gary Pellston, CMA

Style: Professional Guide

Testimonial: "This book is an indispensable tool for anyone on an HOA board. The expert advice and practical approach in 'The Civic Panel Volunteer's Primer' have made a world of difference in our community. Every board member should have a copy!"
— Wanda Orr, HOA Board President

I have uploaded a file as design inspiration but not locked into the colors or look. Just want a clean, professional looking cover.

Target Market(s)

Board members of HOAs (Homeowners associations) in the United States

Industry/Entity Type

Real Estate, HOA

Requirements
Must have
• Clean, professional appearance that conveys authority

```html
<!DOCTYPE html>
<html lang="en">
<head>
<meta charset="utf-8">
<title>The Civic Panel Volunteer's Primer — Cover</title>
<link href="https://fonts.googleapis.com/css2?family=Bebas+Neue&family=Montserrat:wght@300;400&display=swap" rel="stylesheet">
<style>
  :root {
    --backdrop: #2f2b28;
    --paper: #ffffff;
    --ink: #4d4d4d;
    --subtitle-ink: #222222;
    --accent: #f39200;
    --art-yellow: #f8dca6;
    --art-red: #f2a3ae;
    --art-blue: #a6dcf1;
    --art-coral: #f5b3ad;
  }
  * { margin: 0; padding: 0; box-sizing: border-box; }
  html, body {
    width: 1200px;
    height: 1200px;
    overflow: hidden;
    background: var(--backdrop);
  }
  .stage {
    position: relative;
    width: 1200px;
    height: 1200px;
  }
  .cover {
    position: absolute;
    left: 241px;
    top: 62px;
    width: 718px;
    height: 1076px;
    background: var(--paper);
    color: var(--ink);
    overflow: hidden;
  }
  .title {
    position: absolute;
    left: 62px;
    top: 74px;
    font-family: "Bebas Neue", "Oswald", sans-serif;
    font-weight: 400;
    font-size: 164px;
    line-height: 128.6px;
    letter-spacing: 0;
    color: var(--ink);
    transform: scaleX(0.84);
    transform-origin: left top;
    white-space: nowrap;
  }
  .title-line { display: block; }
  .title-highlight { color: var(--accent); }
  .rule {
    position: absolute;
    left: 65px;
    top: 617px;
    width: 137px;
    height: 5px;
    background: var(--accent);
  }
  .subtitle {
    position: absolute;
    left: 65px;
    top: 628px;
    font-family: "Montserrat", sans-serif;
    font-weight: 300;
    font-size: 28px;
    line-height: 33.5px;
    color: var(--subtitle-ink);
    white-space: nowrap;
  }
  .subtitle-line { display: block; }
  .gear-art {
    position: absolute;
    left: 237px;
    top: 720px;
    width: 435px;
    height: 227px;
    border-radius: 12px;
    background: linear-gradient(90deg, var(--art-yellow) 0%, var(--art-red) 40%, var(--art-blue) 68%, var(--art-coral) 100%);
  }
  .author {
    position: absolute;
    left: 65px;
    top: 965px;
    font-family: "Bebas Neue", "Oswald", sans-serif;
    font-weight: 400;
    font-size: 92px;
    line-height: 1;
    color: var(--ink);
    transform: scaleX(0.94);
    transform-origin: left top;
    white-space: nowrap;
  }
</style>
</head>
<body>
  <main class="stage">
    <article class="cover">
      <h1 class="title">
        <span class="title-line">The <span class="title-highlight">Civic</span></span>
        <span class="title-line">Panel</span>
        <span class="title-line">Volunteer's</span>
        <span class="title-line">Primer</span>
      </h1>
      <div class="rule"></div>
      <p class="subtitle">
        <span class="subtitle-line">Self-Direction</span>
        <span class="subtitle-line">Hints and Sound Routines</span>
      </p>
      <div class="gear-art" role="img" aria-label="Illustration of interlocking coloured gears labelled autonomy, transparency, communication, mediation, collaboration, finance and standards"></div>
      <p class="author">Gary Pellston, CMA</p>
    </article>
  </main>
</body>
</html>
```